Cresthaven Vale Goods & City of Nyssa; Public Forum: "Community in Action & Economic Deve...

To Whom it may concern; My name is Garrett Lyle Pascoe and I am the owner of Cresthaven Vale Goods LLC. I live in eastern Oregon in a town called Ontario. I'm originally from a smaller town 12 miles south of Ontario called Nyssa Oregon and that's where this project or the location of my business is going to be located along with moving my family. My Grandfather started a Beer & Pascoe Wholesaler in 1965 in Nyssa called Marlbrook Supply, my father was second generation owner and I had always planned on being 3rd. Well, with big business changing how things work with business consolidating to spread the cost of debt and Dravco purchase of Kessling Morrow, I wouldn't have been approved to buy(franchise agreement). So, bare with me, I tell you this because this information that you'll need to know for the project. My grandfather and Father built a legacy in Nyssa Oregon and were known for; Ethics and Morals, involvement in the community, fundraisers, donations, charity work, public service (volunteer firefighters), endowment scholarship fundraisers, etc....so my grandfather and dad were and are a big fish in a little pond but both are my hero's.

For the last 17 years I've been involved with the State Medical Marijuana program SMMP. Its operated through; BWA; Bureau of Welfare Affairs @ SCA; State Care Agency. I have seen many changes throughout the program. I have a Medical Marijuana Patient card, several Medical Marijuana Caregiver cards, grower cards but the grower cards have been replaced with a Grow Site Administrator card and I am a GSA. So my trade has been indoor cultivation and growing for patients who aren't able due to either health or the financial burdens that an indoor grow requires. Helping others (patients) find relief in whatever aliment they might be fighting has been very rewarding and I love the science behind growing.
In 2015 Oregon passed reactional Marijuana and it is ran by the SSRB; State Spirits Regulation Board. Governor Kessel of Oregon gave local government (city council) the option of opting out of the program which has a 6 tier system with different licensing. Malheur County in which I lived opted out immediately along with Ontario and Nyssa Oregon. Well, Ontario Oregon lifted the ban about 1 year ago and it was a battle but people have slowly started to sway their opinion towards Cannabis. But, now Ontario Oregon is receiving all of the tax benefits that the SSRB program has to offer along with some city sales taxes on the product and Ontario is thriving. Malheur County and the cities within are the poorest in the state, so the tax benefits will go a long way.

PROJECT; I'm a family man.. my wife and I have 4 kids and have decided to move out of Ontario and to my home town in Nyssa (12 miles south of Ontario). I have been working with the community of Nyssa and the City of Nyssa (City Council, Police Department, Fire Department and Chamber of Commerce) in lifting the ban on reactional Marijuana in Nyssa Oregon. I am only asking for 2 out of the 6 licenses and will explain that along with the local politics and my business plan with some attachments. I have done my homework and leg work with this project but ran into an issue and this Is why I'm seeking outside help on the development of a power point. I finally reached my last step, in which was my presentation to the community and city council. I had put together a power point myself and used that for my presentation (I will send you this power point as well). .

I'm going to be having a Public Forum held In Nyssa Oregon so I can get the community to come out and get the right information and ask questions...I was going to see if you guys would design me a power point presentation....I do have one, but I really want a more professional touch...I can send you; business plan, city council power point and some other information....

Thanks,
Garrett Lyle Pasco
Cresthaven Vale Goods

Target Market(s)

Nyssa Oregon City Council Members and the Community/Citizens of Nyssa Oregon

Font styles to use
Sans Serif

Colors

Designer to choose only greyscale colors for use in the design.

Requirements
Must have
• bullet points; on key topics showing what our intent is and what isn't our intent
• heart and passion; getting Nyssa in which is directly on the border with Idaho who is illegal in both medical and recreational marijuana has been huge. Getting the band lifted the Governor Kessel gave city or counties the option to do has been a daunting task.
• Clarity with no chance of misunderstanding my company's intent; i can send you folks some articles and a power point that i put together for the city council as reference.
• market analysis section; so not only will we be talking about the 3% city sales tax on either my recreational production license or the wholesale license, but we will be my company is donating another 3% with our Neighbourhood Uplift Giving Pool. Also, if we can't get a city sales tax on one of those licenses then my company pledges to up our neighbourhood uplift giving pool another 3% to make that a 6% donation on monthly profits. finally, i would like to show the community of Nyssa in visual aids such as graphs,a basic market analysis on what the state of oregon has been bringing in with the tax benefits from recreational marijuana, the city of Huntington Oregon (close to Ontario and opened up their market a couple years before Ontario Oregon did) and finally Ontario Oregon (12 miles north from Nyssa Oregon) and what they have been bringing in with the tax benefits.
Nice to have
• company logo
• pictures of my family
• pictures of Nyssa Oregon
• some positive uplifting quotes on change, trust and family
Should not have
• no Pictures of Marijuana (out of sight out of mind)

```html
<!DOCTYPE html>
<html lang="en">
<head>
<meta charset="utf-8">
<title>Cresthaven Vale Goods &amp; The City of Nyssa</title>
<link href="https://fonts.googleapis.com/css2?family=Montserrat:wght@400;600;700&family=Open+Sans:wght@400;600;700&display=swap" rel="stylesheet">
<style>
:root{
  --page:#000000;
  --slate:#3d3d3d;
  --slate-dark:#333333;
  --slate-deep:#2b2b2b;
  --gold:#f8c664;
  --gold-soft:#f3c97a;
  --white:#ffffff;
  --ink:#2f2f2f;
  --muted:#d8d8d8;
}
*{margin:0;padding:0;box-sizing:border-box}
html,body{width:1200px;height:2797px;overflow:hidden;background:var(--page)}
body{position:relative;font-family:"Open Sans",Arial,sans-serif;color:var(--white)}
.slide{position:absolute;width:545px;height:306px;overflow:hidden;background:var(--slate)}
.col-l{left:34px}.col-r{left:621px}
.r1{top:38px}.r2{top:381px}.r3{top:724px}.r4{top:1067px}
.r5{top:1410px}.r6{top:1752px}.r7{top:2097px}.r8{top:2441px}
.abs{position:absolute}

/* header */
.head-bar{position:absolute;left:2px;top:20px;width:6px;height:24px;background:var(--gold)}
.head-title{position:absolute;left:23px;top:22px;font-family:"Montserrat",Arial,sans-serif;font-size:17px;font-weight:700;letter-spacing:.2px;text-transform:uppercase;color:var(--white);line-height:20px}
.head-title span{font-weight:400;color:var(--gold)}
.mini-brand{position:absolute;right:16px;top:20px;width:60px;text-align:center}
.mini-brand i{display:block;margin:0 auto 2px;width:12px;height:14px;border:1px solid var(--gold)}
.mini-brand b{display:block;font-family:"Montserrat",Arial,sans-serif;font-weight:400;font-size:4px;color:var(--gold);letter-spacing:.2px}

/* footer */
.foot-line{position:absolute;left:0;right:10px;bottom:8px;height:1px;background:var(--gold)}
.foot-num{position:absolute;right:0;bottom:2px;width:11px;height:12px;background:var(--gold);color:var(--ink);font-size:5px;text-align:center;line-height:12px}

/* brand lockup */
.brand{position:absolute;text-align:center;font-family:"Montserrat",Arial,sans-serif;font-weight:400;color:var(--gold)}
.brand .mark{display:block;margin:0 auto;border:2px solid var(--gold)}
.brand .name{display:block;text-transform:uppercase;letter-spacing:1px}
.brand .tag{display:block;text-transform:uppercase;letter-spacing:.5px}

.photo{position:absolute}
.body-text{font-size:8.3px;line-height:16px;color:var(--white)}
ul.bul{list-style:none}
ul.bul li{position:relative;padding-left:12px}
ul.bul li:before{content:"";position:absolute;left:1px;top:.6em;width:3px;height:3px;border-radius:50%;background:currentColor}
ul.arr li:before{content:"➢";background:none;width:auto;height:auto;top:0;font-size:.9em;left:0}

/* cover */
.cover-bg{position:absolute;inset:0;background:radial-gradient(circle at 50% 50%,#3a3a3a,#262626)}
.cover-frame{position:absolute;left:17px;top:50px;width:511px;height:206px;border:1.5px solid var(--gold)}
.cover-panel{position:absolute;left:155px;top:35px;width:235px;height:235px;background:#383838}

/* quote slide */
.q-frame{position:absolute;left:19px;top:50px;width:510px;height:206px;border:1.5px solid var(--white)}
.q-band{position:absolute;left:0;top:105px;width:545px;height:96px;background:var(--gold)}
.q-text{position:absolute;left:85px;top:115px;width:400px;font-family:"Montserrat",Arial,sans-serif;font-weight:600;font-size:21px;line-height:27px;color:var(--ink)}
.q-mark{position:absolute;font-family:"Montserrat",Arial,sans-serif;font-weight:700;font-size:46px;color:var(--slate);line-height:1}

.card-pledge{position:absolute;top:182px;height:90px;border-radius:9px;background:var(--gold);overflow:hidden;box-shadow:2px 3px 6px rgba(0,0,0,.4)}
.card-pledge h4{background:var(--white);color:var(--ink);font-size:8px;text-align:center;height:17px;line-height:19px;font-weight:700}
.card-pledge p{font-size:7px;line-height:9px;text-align:center;color:var(--ink);padding:5px 8px}

.icon-ring{position:absolute;border:2px solid var(--gold);border-radius:50%}
.stat-big{font-family:"Montserrat",Arial,sans-serif;font-weight:700;color:var(--white)}
.pct{position:absolute;font-family:"Montserrat",Arial,sans-serif;font-weight:700;font-size:29px;color:var(--white);line-height:1}
.pct-label{position:absolute;font-size:7.5px;line-height:8px;color:var(--white)}
</style>
</head>
<body>

<!-- 1 cover -->
<section class="slide col-l r1">
  <div class="cover-bg" role="img" aria-label="Dark ornamental background texture"></div>
  <div class="cover-frame"></div>
  <div class="cover-panel"></div>
  <div class="brand" style="left:155px;top:85px;width:235px">
    <i class="mark" style="width:74px;height:74px"></i>
    <span class="name" style="font-size:17px;margin-top:14px">Cresthaven Vale Goods</span>
    <span class="tag" style="font-size:8px;margin-top:3px">"Cultivating the Future"</span>
  </div>
</section>

<!-- 2 family -->
<section class="slide col-r r1">
  <div class="photo" style="inset:0;background:linear-gradient(180deg,#6f5a4a 0%,#4d3e36 55%,#1f1a18 100%)" role="img" aria-label="Family portrait of the owner, his wife and three children at home"></div>
  <div class="brand" style="left:10px;top:14px;width:110px">
    <i class="mark" style="width:26px;height:30px;border-width:1.5px;border-color:#e8e8e8"></i>
    <span class="name" style="font-size:8px;margin-top:4px;color:#e8e8e8;letter-spacing:.3px">Cresthaven Vale Goods</span>
    <span class="tag" style="font-size:4px;color:#e8e8e8">"Cultivating the Future"</span>
  </div>
  <div class="abs" style="left:0;width:545px;top:238px;text-align:center;font-family:'Montserrat',Arial,sans-serif;font-weight:700;font-size:21px">Cresthaven V-G &amp; The City of Nyssa</div>
  <div class="abs" style="left:0;width:545px;top:265px;text-align:center;font-size:9px">"Community In Action, Control, Transparent and Economic Development"</div>
  <div class="abs" style="left:250px;top:282px;width:44px;height:2px;background:var(--gold)"></div>
</section>

<!-- 3 agenda -->
<section class="slide col-l r2" style="background:var(--white)">
  <div class="photo" style="left:0;top:0;width:187px;height:135px;background:linear-gradient(180deg,#8aa3b8 0%,#c9b08a 45%,#4d5d6a 100%)" role="img" aria-label="Lake and rocky canyon at sunset near Nyssa"></div>
  <div class="abs" style="left:0;top:135px;width:187px;height:171px;background:var(--slate)"></div>
  <div class="abs" style="left:87px;top:68px;width:151px;height:40px;background:var(--white);box-shadow:2px 4px 8px rgba(0,0,0,.35);font-family:'Montserrat',Arial,sans-serif;font-weight:600;font-size:20px;color:var(--ink);text-align:center;line-height:40px">AGENDA</div>
  <div class="brand" style="left:0;top:187px;width:187px">
    <i class="mark" style="width:26px;height:30px;border-width:1.5px"></i>
    <span class="name" style="font-size:10px;margin-top:4px;letter-spacing:.3px">Cresthaven Vale Goods</span>
    <span class="tag" style="font-size:4px">"Cultivating the Future"</span>
  </div>
  <div class="abs" style="left:187px;top:0;width:6px;height:306px;background:var(--gold)"></div>
  <ol class="abs" style="list-style:none;left:280px;top:60px;font-size:8.8px;line-height:24.6px;color:var(--ink);font-weight:600">
    <li>01. COMPANY SUMMARY</li><li>02. MISSION STATEMENT</li><li>03. KNOW YOUR BUSINESS LICENSE TYPES</li><li>04. TYPE OF LICENSSING</li><li>05. GOALS</li><li>06. MARKET REVIEW AND TAX BENEFITS</li><li>07. OVERVIEW STATEMENT</li><li>08. MY INTERNAL GRATITUDE AND DEEP</li><li style="padding-left:20px">THOUGHTS W/ GARRETT PASCOE</li>
  </ol>
</section>

<!-- 4 quote -->
<section class="slide col-r r2">
  <div class="q-frame"></div>
  <div class="q-band"></div>
  <div class="q-mark" style="left:24px;top:112px">“</div>
  <p class="q-text">Ethics is knowing the difference between what you have a right to do and what is right to do.</p>
  <div class="q-mark" style="left:487px;top:166px">”</div>
</section>

<!-- 5 company summary -->
<section class="slide col-l r3">
  <div class="head-bar"></div>
  <h2 class="head-title">Company <span>Summary</span></h2>
  <div class="mini-brand"><i></i><b>CRESTHAVEN VALE GOODS</b></div>
  <div class="abs" style="left:23px;top:52px;font-family:'Montserrat',Arial,sans-serif;font-weight:700;font-size:40px;color:#777;line-height:1">“</div>
  <p class="abs body-text" style="left:23px;top:86px;width:500px;text-align:justify">Cresthaven vale goods will be modeled after my father and grandfather business practices. One of our main goals will be to earn the community of Nyssa's trust through our actions. Community involvement, drug awareness, and becoming a member of the chamber would honor our company and being able to give back to a community that gave me a safe and amazing childhood.</p>
  <div class="abs" style="left:490px;top:132px;font-family:'Montserrat',Arial,sans-serif;font-weight:700;font-size:40px;color:#777;line-height:1">”</div>
  <div class="card-pledge" style="left:57px;width:128px"><h4>PLEDGE#1</h4><p>VG cant stress this enough and remains committed to keeping cannabis 100% out of the hands of all youths.</p></div>
  <div class="card-pledge" style="left:208px;width:273px"><h4>PLEDGE#2</h4><p>VG has no interest or would we ever try to change ones believes or core values and is not interested in making this a moral or ethical issue. Marijuana is a drug and it needs to be controlled and we feel that taking control and holding others accountable is the best way to handle this situation.</p></div>
  <div class="foot-line"></div><div class="foot-num">5</div>
</section>

<!-- 6 mission -->
<section class="slide col-r r3">
  <div class="head-bar"></div>
  <h2 class="head-title">Mission <span>Statement</span></h2>
  <div class="mini-brand"><i></i><b>CRESTHAVEN VALE GOODS</b></div>
  <div class="icon-ring" style="left:234px;top:66px;width:58px;height:58px">
    <svg width="54" height="54" viewBox="0 0 54 54"><path d="M34 17 L37 20 L26 33 L21 28 Z" fill="none" stroke="#f8c664" stroke-width="2.4" stroke-linejoin="round"/><path d="M20 30 L16 36 M24 34 L18 38" stroke="#f8c664" stroke-width="2.4" stroke-linecap="round"/></svg>
  </div>
  <ul class="abs bul body-text" style="left:18px;top:140px;width:270px;text-align:justify;font-size:8px;line-height:16.3px"><li>To create a name brand of the highest of quality, with an emphasis on medical applications that holds CONTROL and the strict regulations governed by the city of Nyssa and the SSRB. In doing this; we will bring economic development, growth, family waged jobs and several new tax benefits that can greatly increase the prosperity of Nyssa.</li></ul>
  <div class="abs" role="img" aria-label="Company seal" style="left:325px;top:66px;width:197px;height:197px;border-radius:50%;background:radial-gradient(circle at 40% 35%,#f2d27f,#c9973e 70%,#a77a2c)"></div>
  <div class="foot-line"></div><div class="foot-num">6</div>
</section>

<!-- 7 license types -->
<section class="slide col-l r4">
  <div class="abs" style="left:0;top:0;width:382px;height:306px;background:var(--white)"></div>
  <div class="abs" style="left:382px;top:0;width:3px;height:306px;background:var(--gold)"></div>
  <h2 class="abs" style="left:22px;top:22px;font-family:'Montserrat',Arial,sans-serif;font-weight:700;font-size:17px;color:var(--ink)">KNOW YOUR <span style="color:var(--gold);font-weight:600">BUSINESS LICENSE TYPES</span></h2>
  <div class="abs" style="left:48px;top:68px;width:310px;font-size:6.3px;line-height:9.5px;color:var(--ink)">
    <b style="display:block;margin-bottom:4px">SSRB Licenses</b>
    <ul class="bul">
      <li><b>Producer:</b><br>Ability to plant, cultivate, grow, harvest, and dry marijuana.</li>
      <li><b>Processor:</b><br>Ability to process, compound, or convert marijuana into cannabinoid products, concentrates, and/or extracts.</li>
      <li><b>Wholesale:</b><br>Can purchase quantities of marijuana from other licensed facilities and sell the products to licensed retailers, processors, producers, other wholesalers, or research certificate holders.</li>
      <li><b>Laboratory:</b><br>Accredited by SLAB and responsible for testing marijuana items for pesticides, solvents or residual solvents, tetrahydrocannabinol and cannabidiol concentration, and for microbiological or other contaminants.</li>
      <li><b>Retail:</b><br>Can sell or deliver marijuana items directly to consumers.</li>
      <li><b>Research Certificate:</b><br>Ability to research marijuana for the purpose of benefiting the state's cannabis industry, medical research, or public health and safety.</li>
    </ul>
  </div>
  <div class="mini-brand"><i></i><b>CRESTHAVEN VALE GOODS</b></div>
  <div class="abs" style="left:393px;top:132px;width:145px;height:40px;border:1.5px solid var(--gold);font-family:'Montserrat',Arial,sans-serif;font-weight:700;font-size:19px;letter-spacing:2px;text-align:center;line-height:37px">SECTION 1</div>
  <div class="foot-line" style="left:385px"></div><div class="foot-num">7</div>
</section>

<!-- 8 type of licensing -->
<section class="slide col-r r4">
  <div class="head-bar"></div>
  <h2 class="head-title">Type of <span>Licenssing</span></h2>
  <div class="mini-brand"><i></i><b>CRESTHAVEN VALE GOODS</b></div>
  <div class="abs" style="left:25px;top:72px;width:232px;height:206px;background:var(--white);border-radius:12px;color:var(--ink);text-align:center">
    <div style="font-family:'Montserrat',Arial,sans-serif;font-weight:600;font-size:15px;letter-spacing:1.5px;margin-top:10px">PRODUCTION</div>
    <div style="width:40px;height:2px;background:var(--gold);margin:4px auto 8px"></div>
    <div class="icon-ring" style="position:relative;margin:0 auto;width:40px;height:40px;border-color:var(--ink)">
      <svg width="36" height="36" viewBox="0 0 36 36"><circle cx="18" cy="18" r="6" fill="none" stroke="#2f2f2f" stroke-width="1.6"/><circle cx="18" cy="18" r="10" fill="none" stroke="#2f2f2f" stroke-width="2.5" stroke-dasharray="3 2.5"/></svg>
    </div>
    <div style="font-size:8.5px;line-height:16.5px;margin-top:14px">Strictly indoor tier 1<br>Zoned for out of sight out of mind policy<br>No advertising<br>No traffic<br>Contain smell<br>Strong security</div>
  </div>
  <div class="abs" style="left:253px;top:72px;width:292px;height:206px;background:var(--gold);color:var(--ink)">
    <div style="text-align:center;font-family:'Montserrat',Arial,sans-serif;font-weight:600;font-size:15px;letter-spacing:1.5px;margin-top:10px">WHOLSALE</div>
    <div class="icon-ring" style="position:relative;margin:10px auto 0;width:40px;height:40px;border-color:var(--ink)">
      <svg width="36" height="36" viewBox="0 0 36 36"><circle cx="18" cy="18" r="9" fill="none" stroke="#2f2f2f" stroke-width="1.6"/><path d="M9 18 H27 M18 9 C13 14 13 22 18 27 C23 22 23 14 18 9" fill="none" stroke="#2f2f2f" stroke-width="1.4"/></svg>
    </div>
    <ul class="bul arr" style="font-size:7.5px;line-height:14px;padding:10px 14px 0 20px">
      <li>Ship, test and wholesale product out of the area</li>
      <li>Pledges to not create problems for the city of Nyssa; no extra traffic of any kind</li>
      <li>No advertising</li>
      <li>Never glorifying to our youth</li>
      <li>Wholesale out of the area to guarantee product gets turned into processing and medical applications</li>
      <li>In support of abolishment of the black-market</li>
    </ul>
  </div>
  <div class="foot-line"></div><div class="foot-num">8</div>
</section>

<!-- 9 business assumptions -->
<section class="slide col-l r5">
  <div class="photo" style="inset:0;background:linear-gradient(180deg,#4a4a4a 0%,#3a3a3a 60%,#2e2e2e 100%)" role="img" aria-label="Muted family portrait of the owner with his wife and children"></div>
  <div class="brand" style="left:14px;top:22px;width:140px">
    <i class="mark" style="width:36px;height:40px"></i>
    <span class="name" style="font-size:10px;margin-top:5px;letter-spacing:.3px">Cresthaven Vale Goods</span>
    <span class="tag" style="font-size:5px">"Cultivating the Future"</span>
  </div>
  <div class="abs" style="right:30px;top:200px;text-align:right;font-family:'Montserrat',Arial,sans-serif;font-weight:700;font-size:23px;line-height:29px">BUSINESS<br>ASSUMPTIONS &amp; GOALS</div>
  <div class="abs" style="right:30px;top:262px;font-size:7.5px">Opportunity, creating growth and prosperity to the community of Nyssa</div>
  <div class="abs" style="right:0;top:205px;width:8px;height:52px;background:var(--gold)"></div>
</section>

<!-- 10 goals -->
<section class="slide col-r r5">
  <div class="head-bar"></div>
  <h2 class="head-title">Goals &amp; Main Bullet <span>Points</span></h2>
  <div class="mini-brand"><i></i><b>CRESTHAVEN VALE GOODS</b></div>
  <ul class="abs bul" style="left:23px;top:56px;width:505px;font-size:7.2px;line-height:12.2px">
    <li>Family Wage Jobs</li>
    <li>Intracellular part of the community of Nyssa (like my grandfather and father before me).</li>
    <li>Give back to the community; participating and organizing awareness and fundraisers for drug abuse and other areas in which the community could use extra funding,</li>
    <li>Create additional revenue; city tax &amp; neighbourhood uplift giving pool</li>
    <li style="color:var(--gold);font-weight:700">STRICTLY INDOOR PRODUCTION FACILTY; <span style="color:var(--white);font-weight:400">with an out of sight out of mind policy,</span> NO ADVERTISING, NO GLORFYING</li>
    <li>full compliance with SSRB and City of Nyssa regulatory agencies, tackling within a pending status any and all concerns pending walkthrough with SSRB; ODOR CONCERNS, SECURITY CONCERNS, ETC.</li>
    <li><b style="color:var(--gold)">NOT ASKING FOR A RETAIL OPERATION;</b> traffic and flux of people is not something we are seeking but trying to avoid</li>
    <li><b style="color:var(--gold)">PRODUCT WILL BE TAKEN OUT OF THE AREA (ACROSS THE STATE),</b> This alleviates and helps VG guarantee that our product will not be getting into the hands of our children.</li>
    <li>Allocation of funds for a swimming pool</li>
    <li>Work and build healthy working relationships with the Nyssa chamber of commerce, Nyssa police department, fire department and city council</li>
    <li>100% committed in fundraisers in all aspects; drug awareness, Nyssa downtown</li>
    <li>Revitalization, endowment scholarships, etc.</li>
  </ul>
  <div class="foot-line"></div><div class="foot-num">10</div>
</section>

<!-- 11 market review -->
<section class="slide col-l r6">
  <div class="head-bar"></div>
  <h2 class="head-title">Market Review <span>and Tax Benefits</span></h2>
  <div class="mini-brand"><i></i><b>CRESTHAVEN VALE GOODS</b></div>
  <div class="abs" style="left:0;top:69px;width:200px;height:222px;background:var(--gold);padding:16px 12px 0 23px;font-family:'Montserrat',Arial,sans-serif;font-weight:600;font-size:10.5px;line-height:20.5px;color:var(--ink)">
    <span style="color:var(--white)">At the request of the council;</span><br>( I will have a market analysis done on Nyssa with factual numbers and data of tax benefits that a recreational indoor production facility could create for the community ).
  </div>
  <div class="abs" style="left:200px;top:115px;width:345px;height:1px;background:#8a8a8a"></div>
  <div class="abs" style="left:200px;top:171px;width:345px;height:1px;background:#8a8a8a"></div>
  <div class="abs" style="left:200px;top:222px;width:345px;height:1px;background:#8a8a8a"></div>
  <div class="abs" style="left:245px;top:77px"><span class="stat-big" style="font-size:30px">3%</span> <span style="display:inline-block;font-size:8.5px;line-height:9px;vertical-align:3px">city sales<br>tax</span></div>
  <div class="abs" style="left:245px;top:123px;font-size:10px">Conservative base point around,</div>
  <div class="abs" style="left:245px;top:136px"><span class="stat-big" style="font-size:30px">$100,000</span> <span style="font-size:9px">a month</span></div>
  <div class="abs" style="left:240px;top:185px"><span style="font-size:9.5px">Community action fund donating another</span> <span class="stat-big" style="font-size:27px">3%</span></div>
  <div class="abs" style="left:245px;top:232px;font-size:10px">Potential grand total of,</div>
  <div class="abs" style="left:245px;top:246px"><span class="stat-big" style="font-size:30px">$6,000</span> <span style="font-size:9px">a month to Nyssa</span></div>
  <div class="foot-line"></div><div class="foot-num">11</div>
</section>

<!-- 12 intent -->
<section class="slide col-r r6" style="background:var(--gold)">
  <div class="abs" style="left:30px;top:27px;width:253px;height:249px;border:2px solid var(--white)"></div>
  <div class="abs" style="left:100px;top:17px;background:var(--gold);padding:0 12px;font-family:'Montserrat',Arial,sans-serif;font-size:17px;color:var(--ink)"><b>MY</b> INTENT</div>
  <ul class="abs bul arr" style="left:60px;top:60px;width:210px;font-size:7.3px;line-height:9.6px;color:var(--ink)">
    <li>Family wage jobs</li>
    <li>Engaged in the community; fundraising, drug awareness.</li>
    <li>Support the Nyssa chamber revitalization of downtown.</li>
    <li>Donate/allocate funds into obtaining more activates for our youth-swimming pool!</li>
    <li>Create additional tax revenue &amp; additional funds w/VG neighbourhood uplift giving pool</li>
    <li>Strictly indoor production facility; contain smell, strong security, no advertising &amp; operate w/"out of sight, out of mind policy."</li>
    <li>VG will not add or create traffic</li>
    <li>Wholesale our product out of the area; our company pledges to keep our product from being unattainable to our youths.</li>
    <li>100% transparent</li>
  </ul>
  <div class="abs" style="left:8px;top:148px;width:44px;height:44px;border-radius:50%;background:var(--slate)">
    <svg width="44" height="44" viewBox="0 0 44 44"><rect x="12" y="21" width="5" height="11" fill="#fff"/><path d="M19 21 L23 13 C25 12 26 14 25.5 16 L24.5 20 H31 C33 20 33.5 22 33 23.5 L31 31 C30.6 32 30 32 29 32 H19 Z" fill="#fff"/></svg>
  </div>
  <div class="abs" style="left:393px;top:20px;width:44px;height:44px;border-radius:50%;background:var(--slate)">
    <svg width="44" height="44" viewBox="0 0 44 44"><g transform="rotate(180 22 22)"><rect x="12" y="21" width="5" height="11" fill="#fff"/><path d="M19 21 L23 13 C25 12 26 14 25.5 16 L24.5 20 H31 C33 20 33.5 22 33 23.5 L31 31 C30.6 32 30 32 29 32 H19 Z" fill="#fff"/></g></svg>
  </div>
  <div class="abs" style="left:352px;top:72px;width:130px;text-align:center;font-family:'Montserrat',Arial,sans-serif;font-size:16px;color:var(--ink)"><b>NOT</b> MY INTENT</div>
  <ul class="abs bul arr" style="left:315px;top:106px;width:210px;font-size:7.3px;line-height:18.5px;color:var(--ink)">
    <li>Not opening a retail operation or the following: medical marijuana dispensary, pot shop or anything downtown main street</li>
    <li>No glorifying or advertising our company in the surrounding area</li>
    <li>Not asking/seeking nor am ever seeking outside grows rather than indoor</li>
    <li>Not creating additional traffic or flux of people migrating into Nyssa</li>
  </ul>
  <div class="foot-line" style="background:var(--slate)"></div><div class="foot-num" style="background:var(--slate);color:var(--white)">12</div>
</section>

<!-- 13 taxes -->
<section class="slide col-l r7">
  <div class="head-bar"></div>
  <h2 class="head-title" style="font-size:15.5px">Where do the taxes on rec pot go in <span>Oregon?</span></h2>
  <div class="mini-brand"><i></i><b>CRESTHAVEN VALE GOODS</b></div>
  <div class="pct" style="left:28px;top:104px">40%</div><div class="pct-label" style="left:96px;top:110px">To common<br>School fund</div>
  <div class="pct" style="left:28px;top:158px">20%</div><div class="pct-label" style="left:96px;top:160px">To mental health<br>Alcoholism and<br>Drug services</div>
  <div class="pct" style="left:32px;top:212px">15%</div><div class="pct-label" style="left:96px;top:215px">To state<br>Police</div>
  <div class="abs" role="img" aria-label="Green leaf illustration" style="left:205px;top:90px;width:135px;height:140px;border-radius:50%;background:radial-gradient(circle,#9fc3ad,#8db39c 60%,rgba(141,179,156,0) 72%)"></div>
  <div class="pct" style="left:456px;top:104px">5%</div><div class="pct-label" style="left:340px;top:103px;width:112px;text-align:right">To State Care<br>Agency for alcohol and<br>drug abuse prevention</div>
  <div class="pct" style="left:456px;top:158px">10%</div><div class="pct-label" style="left:340px;top:160px;width:112px;text-align:right">To Counties for<br>Enforcement of<br>the measure</div>
  <div class="pct" style="left:456px;top:212px">10%</div><div class="pct-label" style="left:340px;top:214px;width:112px;text-align:right">To Cities for<br>Enforcement of<br>the measure</div>
  <div class="foot-line"></div><div class="foot-num">13</div>
</section>

<!-- 14 overview -->
<section class="slide col-r r7">
  <div class="head-bar"></div>
  <h2 class="head-title">Overview <span>Statement</span></h2>
  <div class="mini-brand"><i></i><b>CRESTHAVEN VALE GOODS</b></div>
  <div class="icon-ring" style="left:234px;top:64px;width:60px;height:60px">
    <svg width="56" height="56" viewBox="0 0 56 56"><circle cx="28" cy="28" r="15" fill="none" stroke="#f8c664" stroke-width="2.5"/><circle cx="28" cy="28" r="8" fill="none" stroke="#f8c664" stroke-width="2.5"/><circle cx="28" cy="28" r="2.5" fill="#f8c664"/><path d="M28 28 L40 16 M37 14 L42 14 L42 19" stroke="#f8c664" stroke-width="2.2" fill="none"/></svg>
  </div>
  <ul class="abs bul arr body-text" style="left:18px;top:140px;width:510px;font-size:8px;line-height:16.3px">
    <li>Doing this on a professional manner while following all the state guidelines in which the State Spirits Regulation Board has set forth. Along with the city of Nyssa</li>
    <li>Cresthaven vale goods is Not asking for a retail license, as we feel this would an abrupt change to Nyssa with to much change to fast with increased traffic and a abundance of people. Pros and cons can be debated and discussed. It is of my opinion that some caution and restrain can still be and should be practiced when introducing the community to these new waters.</li>
    <li>Willing to form a Pac committee to help eliminate the black market and create a positive impact on the community while never advertising or glorifying to our youth.</li>
  </ul>
  <div class="foot-line"></div><div class="foot-num">14</div>
</section>

<!-- 15 gratitude -->
<section class="slide col-l r8">
  <div class="head-bar"></div>
  <h2 class="head-title" style="font-size:16px;line-height:20px">My internal gratitude and deep<br>thoughts w/ <span>Garrett Pascoe</span></h2>
  <div class="mini-brand"><i></i><b>CRESTHAVEN VALE GOODS</b></div>
  <p class="abs body-text" style="left:30px;top:88px;width:242px;text-align:justify;font-size:9px;line-height:18.2px">I know what the community and the council have had to endear in the past with the out of state cards, unwanted traffic, pressure on community/council along with the black-market and all the risks that alone brings to our youths. So, thank you for not grouping me with those individuals and allowing me to give this presentation in which will be taking a very different approach.</p>
  <div class="abs" style="left:335px;top:78px;width:133px;height:176px;background:var(--gold)"></div>
  <div class="photo" style="left:347px;top:90px;width:138px;height:176px;background:linear-gradient(180deg,#7b6a66,#b98d86 50%,#5e5252);box-shadow:2px 3px 6px rgba(0,0,0,.4)" role="img" aria-label="Baby in a holiday hat lying on a plaid blanket"></div>
  <div class="foot-line"></div><div class="foot-num">15</div>
</section>

<!-- 16 thank you -->
<section class="slide col-r r8">
  <div class="photo" style="inset:0;background:linear-gradient(180deg,#c7a48a 0%,#a27d6c 45%,#5a4f58 75%,#2d2833 100%)" role="img" aria-label="Family walking together across a snowy field at sunset"></div>
  <div class="brand" style="left:14px;top:25px;width:110px">
    <i class="mark" style="width:30px;height:34px"></i>
    <span class="name" style="font-size:8.5px;margin-top:4px;letter-spacing:.3px">Cresthaven Vale Goods</span>
    <span class="tag" style="font-size:4px">"Cultivating the Future"</span>
  </div>
  <p class="abs" style="left:0;width:545px;top:252px;text-align:center;font-family:'Montserrat',Arial,sans-serif;font-weight:700;font-size:12.5px;line-height:16px">Thank you for giving me your time today, and letting me present the<br>future of Nyssa to you my fellow community, and council members.</p>
</section>

</body>
</html>
```